Website for boutique digital agency helping high-tech startups accelerate growth.

We need a website design for a relatively young company based in Mauritius called 'LumaTrel'.

We are a professional services firm delivering digital infrastructure for revenue operations (RevOps)*.

Entrepreneurial startups and SMBs in the technology sector work with us to accelerate growth by delivering extraordinary customer experiences across the full customer lifecycle.

We would like a colourful design that utilises the (4) colours of our existing logo design.

The final design should communicate dynamic growth through relentless customer focus.
----------------------------------------------------------
*Revenue Operations (RevOps) is the strategic alignment of sales, marketing and customer success operations to accelerate growth by delivering extraordinary customer experiences across the full customer life cycle.

Target Market(s)

Entrepreneurial startups and SMBs (Small/Medium Businesses) in the technology sector.

Question: Why the technology sector?

Answer: Because technology entrepreneurs often have a tremendous challenge to effectively communicate to the market and to prospective customers the value and the benefits of their products & services due to the inherent complexity of technological innovation.

LumaTrel is a team of creatively-minded engineers and technologists who have worked with and understand the technologies and innovations our clients are passionate about bringing to market.

Industry/Entity Type

Professional Service

Number of Pages Required

5+ page

Font styles to use
Sans Serif

Requirements
Must have
• Minimalistic designs rich with visual meaning are highly preferred. Mobile responsive designs are also required. Must show how designs render on Desktop, Tablet and Smartphone devices.

Website pages:
1) Homepage: problem statement, target customers, value proposition & benefits
2) Services: 3-4 tiers of services packages with pricing and "how to work with us"
3) Resources: links to all kinds of relevant materials
4) Contact Us: contact form and special project quote form
5) Blog: matrix design with featured images for each post
Nice to have
• Bold, interesting, colourful, inspiring images that visually communicate:
- relentless customer focus
- extraordinary, memorable experiences
- business at the speed of innovation
Should not have
• Any meme or theme that panders to "political correctness".

```html
<!DOCTYPE html>
<html lang="en">
<head>
<meta charset="utf-8">
<title>LumaTrel — Presentation</title>
<link rel="stylesheet" href="https://fonts.googleapis.com/css2?family=Poppins:wght@300;400;500;600;700;800&display=swap">
<style>
:root{
  --teal:#1b8a84;
  --teal-band:#18827c;
  --teal-deep:#137069;
  --teal-dark:#0f5d66;
  --orange:#f15a24;
  --lime:#8dc63f;
  --red:#e4202f;
  --ink:#1f2a30;
  --muted:#6c767c;
  --line:#e7ecee;
  --soft:#f3f5f6;
  --ghost:#e3e3e3;
  --white:#ffffff;
}
*{box-sizing:border-box;margin:0;padding:0}
html,body{width:1200px;height:4042px;overflow:hidden}
body{background:var(--white);font-family:'Poppins',sans-serif;color:var(--ink);position:relative}

/* ===== presentation board ===== */
.band{position:absolute;left:0;top:0;width:1200px;height:580px;background:var(--teal-band);overflow:hidden}
.band-title{position:absolute;left:0;top:44px;width:1200px;text-align:center;color:var(--white);font-size:74px;font-weight:400;line-height:62px}
.label{position:absolute;font-weight:400;text-align:center;line-height:1}
.label.mobile-label{left:900px;top:396px;width:200px;color:var(--white);font-size:39px;line-height:40px}
.label.home-label{left:286px;top:795px;width:400px;color:var(--ink);font-size:39px}
.thanks{position:absolute;left:218px;top:2960px;font-size:112px;font-weight:600;line-height:118px;color:var(--ghost);letter-spacing:2px}

.screen{position:absolute;overflow:hidden;background:var(--white)}
.screen.desktop{left:191px;top:216px;width:652px;height:369px;outline:14px solid #1c1c1c}
.screen.homepage{left:242px;top:839px;width:488px;height:1939px;box-shadow:0 4px 18px rgba(0,0,0,.22)}
.screen.mobile{left:883px;top:491px;width:233px;height:3424px;border:3px solid #1c1c1c;border-radius:22px;box-shadow:0 4px 18px rgba(0,0,0,.2)}

.scaler{position:absolute;left:0;top:0;width:1200px;transform-origin:0 0}
.desktop .scaler{height:680px;transform:scale(.5433)}
.homepage .scaler{height:4768px;transform:scale(.4067)}

/* ===== desktop site ===== */
.site{position:relative;width:1200px;font-family:'Poppins',sans-serif}
.section{position:absolute;left:0;width:1200px;overflow:hidden}
.btn{display:inline-block;background:var(--orange);color:var(--white);font-weight:600;font-size:13px;letter-spacing:1px;padding:12px 26px;text-transform:uppercase}
.eyebrow{font-size:20px;color:var(--teal);text-align:center}
.title{font-size:36px;font-weight:400;color:var(--teal);text-align:center;line-height:1.2}
p.body{font-size:14px;line-height:1.7;color:var(--muted)}

.hero{top:0;height:680px}
.brand{position:absolute;left:110px;top:26px;display:flex;align-items:center;gap:10px;font-weight:700;font-size:22px;color:var(--teal-dark)}
.brand i{width:18px;height:18px;border-radius:50%;background:var(--orange);display:block}
.nav{position:absolute;left:440px;top:30px;display:flex;gap:32px;font-size:14px;color:var(--teal)}
.nav .active{color:var(--orange)}
.phone{position:absolute;right:40px;top:30px;font-size:14px;font-weight:600;color:var(--red);display:flex;gap:8px;align-items:center}
.hero-copy{position:absolute;left:110px;top:190px;width:440px}
.hero-copy .pre{font-size:22px;color:var(--ink)}
.hero-copy .boutique{font-size:44px;color:var(--ink);line-height:1.1}
.hero-copy h1{font-size:70px;font-weight:800;color:var(--teal-dark);line-height:1}
.hero-copy p{margin:22px 0 26px;font-size:14px;line-height:1.6;color:var(--muted);width:420px}
.hero-art{position:absolute;right:0;top:0}
.hero-accent{position:absolute;left:0;top:190px}

.features{top:637px;height:637px}
.features .eyebrow{position:absolute;top:100px;left:0;right:0}
.features .title{position:absolute;top:128px;left:0;right:0}
.cards{position:absolute;top:255px;left:185px;right:185px;display:flex;justify-content:space-between}
.card{width:188px;height:235px;background:var(--white);box-shadow:0 8px 26px rgba(0,0,0,.08);padding:22px 18px}
.card h4{font-size:14px;font-weight:500;line-height:1.3;color:var(--ink);height:44px}
.card .ico{width:60px;height:60px;border-radius:50%;margin:12px 0 28px;display:flex;align-items:center;justify-content:center}
.card .rule{width:26px;height:2px;background:var(--line);margin-bottom:10px}
.card p{font-size:12px;line-height:1.5;color:var(--muted)}
.ring{position:absolute;left:40px;top:180px}

.value{top:1274px;height:513px;background:var(--soft)}
.value .copy{position:absolute;left:155px;top:140px;width:440px}
.value h2,.problem h2{font-size:40px;font-weight:400;color:var(--teal);line-height:1.1;margin-bottom:18px}
.value .art{position:absolute;right:0;top:22px}

.problem{top:1787px;height:645px}
.problem .art{position:absolute;left:0;top:75px}
.problem .copy{position:absolute;left:605px;top:205px;width:440px}

.packages{top:2432px;height:637px}
.packages .eyebrow{position:absolute;top:82px;left:0;right:0}
.packages .title{position:absolute;top:108px;left:0;right:0;font-weight:700;color:var(--teal-dark);font-size:38px}
.plans{position:absolute;top:180px;left:155px;right:155px;display:flex;justify-content:space-between;align-items:flex-start}
.plan{width:270px;background:var(--white);box-shadow:0 8px 26px rgba(0,0,0,.08);text-align:center;padding:44px 20px 40px;margin-top:24px}
.plan.featured{background:var(--teal-dark);margin-top:0;padding:64px 20px 76px;width:300px}
.plan .name{font-size:15px;color:var(--teal)}
.plan .price{font-size:50px;font-weight:700;color:var(--orange);line-height:1.2}
.plan .price sup{font-size:24px}
.plan ul{list-style:none;font-size:13px;color:var(--muted);line-height:2.1;margin:6px 0 20px}
.plan.featured .name,.plan.featured ul{color:var(--white)}
.plan.featured .btn{background:var(--white);color:var(--orange)}
.lime-blob{position:absolute;left:0;top:20px}

.customers{top:3069px;height:347px}
.customers .title{position:absolute;top:70px;left:0;right:0;font-size:34px}
.logos{position:absolute;top:144px;left:155px;right:155px;display:flex;justify-content:space-between}
.logo-tile{width:210px;height:96px;border:1px solid var(--line);display:flex;align-items:center;justify-content:center;gap:10px;font-size:21px;font-weight:600;color:var(--ink)}
.logo-tile i{width:14px;height:14px;background:var(--teal);display:block}
.pager{position:absolute;top:278px;left:0;right:0;display:flex;justify-content:center;gap:8px}
.pager i{width:7px;height:7px;border-radius:50%;background:var(--line);display:block}
.pager i.on{background:var(--teal)}

.blog{top:3416px;height:483px}
.blog .title{position:absolute;top:44px;left:0;right:0;font-size:36px}
.posts{position:absolute;top:108px;left:155px;right:155px;display:flex;justify-content:space-between}
.post{width:285px}
.post .thumb{display:block;width:285px;height:190px}
.post .date{font-size:11px;color:var(--muted);margin:14px 0 4px;text-transform:uppercase}
.post h5{font-size:16px;font-weight:500;line-height:1.4;color:var(--ink)}
.post .more{font-size:11px;font-weight:700;color:var(--teal-dark);margin-top:12px}

.contact{top:3899px;height:475px}
.contact .photo{position:absolute;inset:0}
.contact .form{position:absolute;left:370px;top:90px;width:460px;text-align:center}
.contact h3{font-size:38px;font-weight:400;color:var(--white);margin-bottom:34px}
.fields{display:grid;grid-template-columns:1fr 1fr;gap:30px 30px;text-align:left}
.field{font-size:12px;color:var(--white);border-bottom:1px solid rgba(255,255,255,.7);padding-bottom:6px}
.contact .btn{margin-top:34px}

.footer{top:4374px;height:394px}
.cols{position:absolute;top:50px;left:155px;right:155px;display:flex;justify-content:space-between}
.col h6{font-size:13px;font-weight:700;color:var(--teal-dark);margin-bottom:14px;text-transform:uppercase}
.col p,.col li{font-size:12px;line-height:1.8;color:var(--teal)}
.col ul{list-style:none}
.col.about{width:250px}
.contact-line{display:flex;align-items:center;gap:8px;font-size:12px;color:var(--teal-dark);margin-top:8px}
.connect{font-size:12px;font-weight:700;color:var(--teal-dark);margin-top:14px}
.socials{display:flex;gap:10px;margin-top:8px}
.socials i{width:14px;height:14px;border-radius:50%;background:var(--teal);display:block}
.news input{display:block;width:220px;height:36px;border:1px solid var(--line);background:var(--soft);font-family:inherit;font-size:12px;padding:0 10px;margin:10px 0 14px}
.copyright{position:absolute;bottom:28px;left:155px;right:155px;text-align:center;font-size:12px;color:var(--teal-dark);border-top:1px solid var(--line);padding-top:18px}

/* ===== mobile site ===== */
.m{position:absolute;left:0;width:100%}
.m-center{text-align:center}
.m-brand{left:10px;top:12px;width:auto;display:flex;align-items:center;gap:5px;font-size:10px;font-weight:700;color:var(--teal-dark)}
.m-brand i{width:9px;height:9px;border-radius:50%;background:var(--orange);display:block}
.m-menu{left:auto;right:10px;top:10px;width:16px;height:16px;border:1px solid var(--line);border-radius:50%}
.m-pre{left:11px;top:178px;font-size:15px;color:var(--ink)}
.m-boutique{left:11px;top:198px;font-size:24px;color:var(--ink);line-height:1}
.m-h1{left:11px;top:222px;font-size:29px;font-weight:800;line-height:29px;color:var(--teal-dark)}
.m-btn{position:absolute;background:var(--orange);color:var(--white);font-size:11px;font-weight:600;letter-spacing:.5px;text-transform:uppercase;display:flex;align-items:center;justify-content:center}
.m-eyebrow{font-size:15px;color:var(--teal);line-height:1}
.m-title{font-size:19px;color:var(--teal);line-height:20px}
.m-card{left:21px;top:507px;width:176px;height:202px;background:var(--white);box-shadow:0 6px 18px rgba(0,0,0,.1);padding:30px 12px 0}
.m-card h4{font-size:12.5px;font-weight:500;line-height:1.25;color:var(--ink)}
.m-card .ico{width:46px;height:46px;border-radius:50%;background:var(--teal);margin:12px 0 22px;display:flex;align-items:center;justify-content:center}
.m-card .rule{width:22px;height:2px;background:var(--line);margin-bottom:4px}
.m-card p{font-size:10.5px;line-height:1.3;color:var(--muted)}
.m-arrows{font-size:12px;color:#c4cacd;letter-spacing:10px;line-height:1}
.m-h2{font-size:20px;color:var(--teal);line-height:21px}
.m-text{left:14px;width:205px;font-size:12px;line-height:17px;color:var(--muted);text-align:center}
.m-plan{left:11px;top:1580px;width:210px;height:267px;background:var(--teal-dark);color:var(--white);text-align:center;padding-top:40px}
.m-plan .name{font-size:13px}
.m-plan .price{font-size:38px;font-weight:700;color:var(--orange);line-height:1.2}
.m-plan .price sup{font-size:18px}
.m-plan ul{list-style:none;font-size:11.5px;line-height:23px;margin-top:0}
.m-tile{left:29px;top:1930px;width:175px;height:78px;border:1px solid var(--line);display:flex;align-items:center;justify-content:center;gap:8px;font-size:17px;font-weight:600;color:var(--ink)}
.m-tile i{width:12px;height:12px;background:var(--teal);display:block}
.m-thumb{left:11px;top:2126px;width:212px;height:152px}
.m-date{left:13px;top:2292px;font-size:10px;color:var(--muted);text-transform:uppercase}
.m-post{left:13px;top:2305px;width:210px;font-size:14px;line-height:16px;color:var(--ink)}
.m-more{left:13px;top:2350px;font-size:10px;font-weight:700;color:var(--teal-dark)}
.m-contact{left:0;top:2420px;height:240px}
.m-field{left:55px;width:125px;font-size:9.5px;color:var(--white);border-bottom:1px solid rgba(255,255,255,.6);padding-bottom:3px}
.m-foot h6{font-size:13px;font-weight:700;color:var(--teal-dark);text-transform:uppercase}
.m-foot p,.m-foot li{font-size:10.5px;line-height:16px;color:var(--teal)}
.m-foot ul{list-style:none}
.m-line{left:11px;display:flex;gap:8px;align-items:center;font-size:10.5px;color:var(--teal-dark)}
.m-socials{left:11px;top:2879px;display:flex;gap:12px}
.m-socials i{width:12px;height:12px;border-radius:50%;background:var(--teal);display:block}
.m-input{left:11px;top:3287px;width:190px;height:32px;background:var(--soft);border:1px solid var(--line);font-size:10px;color:var(--ink);padding:9px 8px}
.m-copy{left:0;top:3390px;font-size:9.5px;color:var(--teal-dark);text-align:center}
</style>
</head>
<body>

<svg width="0" height="0" style="position:absolute" aria-hidden="true">
  <defs>
    <linearGradient id="heroPhoto" x1="0" y1="0" x2="1" y2="1"><stop offset="0" stop-color="#f4ece4"/><stop offset=".5" stop-color="#c9a38a"/><stop offset="1" stop-color="#5b4638"/></linearGradient>
    <linearGradient id="valPhoto" x1="0" y1="0" x2="1" y2="1"><stop offset="0" stop-color="#ece7e2"/><stop offset="1" stop-color="#8c7d72"/></linearGradient>
    <linearGradient id="valOrange" x1="0" y1="0" x2="1" y2="1"><stop offset="0" stop-color="#f7931e"/><stop offset="1" stop-color="#f15a24"/></linearGradient>
    <linearGradient id="probPhoto" x1="0" y1="0" x2="1" y2="1"><stop offset="0" stop-color="#4fb3ac"/><stop offset="1" stop-color="#0f5d66"/></linearGradient>
    <linearGradient id="b1" x1="0" y1="0" x2="1" y2="1"><stop offset="0" stop-color="#d8e2dc"/><stop offset="1" stop-color="#4f6b5c"/></linearGradient>
    <linearGradient id="b2" x1="0" y1="0" x2="1" y2="1"><stop offset="0" stop-color="#f5f3f1"/><stop offset="1" stop-color="#b8c2cf"/></linearGradient>
    <linearGradient id="b3" x1="0" y1="0" x2="1" y2="1"><stop offset="0" stop-color="#e3ecf3"/><stop offset="1" stop-color="#8a5a4a"/></linearGradient>
    <linearGradient id="cPhoto" x1="0" y1="0" x2="1" y2="0"><stop offset="0" stop-color="#6f7f86"/><stop offset=".5" stop-color="#d9dde0"/><stop offset="1" stop-color="#8a9499"/></linearGradient>
    <symbol id="phoneIcon" viewBox="0 0 24 24"><path d="M6.6 10.8a15 15 0 0 0 6.6 6.6l2.2-2.2a1 1 0 0 1 1-.25 11.4 11.4 0 0 0 3.6.57 1 1 0 0 1 1 1V20a1 1 0 0 1-1 1A17 17 0 0 1 3 4a1 1 0 0 1 1-1h3.5a1 1 0 0 1 1 1c0 1.25.2 2.45.57 3.57a1 1 0 0 1-.25 1z"/></symbol>
    <symbol id="chipIcon" viewBox="0 0 24 24"><rect x="5" y="5" width="14" height="14" rx="2" fill="none" stroke="#fff" stroke-width="2"/><path d="M9 1v4M15 1v4M9 19v4M15 19v4M1 9h4M1 15h4M19 9h4M19 15h4" stroke="#fff" stroke-width="2"/></symbol>
  </defs>
</svg>

<!-- board background -->
<div class="band">
  <svg width="1200" height="580" viewBox="0 0 1200 580">
    <path d="M0 140 C120 120 240 200 260 330 C280 470 180 560 0 580 Z" fill="var(--teal-deep)" opacity=".55"/>
    <path d="M1200 0 L980 0 C1020 60 1110 90 1200 80 Z" fill="var(--teal-deep)" opacity=".45"/>
  </svg>
  <div class="band-title">LumaTrel<br>Presentation</div>
</div>
<div class="label mobile-label">Mobile<br>Version</div>
<div class="label home-label">Home Page</div>

<!-- ===== desktop hero screen ===== -->
<div class="screen desktop">
  <div class="scaler">
    <div class="site">
      <section class="section hero">
        <svg class="hero-accent" width="90" height="260" viewBox="0 0 90 260"><path d="M0 0 L90 130 L0 260 Z" fill="#fde6dc"/></svg>
        <svg class="hero-art" width="720" height="660" viewBox="0 0 720 660" role="img" aria-label="Photo of a small agency team gathered around a table reviewing work together">
          <path d="M720 0 L230 0 C150 120 140 260 230 380 C320 510 480 620 640 600 C690 592 710 580 720 570 Z" fill="url(#heroPhoto)"/>
          <path d="M250 0 C140 130 150 290 250 400 C330 490 430 540 520 570" fill="none" stroke="#8dc63f" stroke-width="10" stroke-linecap="round"/>
          <path d="M720 520 C690 580 640 620 560 622" fill="none" stroke="#e4202f" stroke-width="8" stroke-linecap="round"/>
        </svg>
        <div class="brand"><i></i>LumaTrel</div>
        <nav class="nav"><span class="active">Home</span><span>Services</span><span>Resources</span><span>Blog</span><span>Contact Us</span></nav>
        <div class="phone"><svg width="14" height="14" fill="#e4202f"><use href="#phoneIcon"/></svg>230-555-0147</div>
        <div class="hero-copy" style="top:220px">
          <div class="pre">We are</div>
          <div class="boutique">Boutique</div>
          <h1>DIGITAL<br>AGENCY</h1>
          <p>Many desktop publishing packages and web page editors now use Lorem Ipsum as their default model text, and a search for 'lorem ipsum'</p>
          <span class="btn">Contact Us</span>
        </div>
      </section>
    </div>
  </div>
</div>

<!-- ===== full home page ===== -->
<div class="screen homepage">
  <div class="scaler">
    <div class="site">

      <section class="section hero" style="height:637px">
        <svg class="hero-accent" width="90" height="260" viewBox="0 0 90 260"><path d="M0 0 L90 130 L0 260 Z" fill="#fde6dc"/></svg>
        <svg class="hero-art" width="720" height="620" viewBox="0 0 720 620" role="img" aria-label="Photo of a small agency team gathered around a table reviewing work together">
          <path d="M720 0 L230 0 C150 120 140 260 230 380 C320 500 480 600 640 585 C690 578 710 568 720 560 Z" fill="url(#heroPhoto)"/>
          <path d="M250 0 C140 130 150 290 250 400 C330 485 430 535 520 560" fill="none" stroke="#8dc63f" stroke-width="10" stroke-linecap="round"/>
        </svg>
        <div class="brand"><i></i>LumaTrel</div>
        <nav class="nav"><span class="active">Home</span><span>Services</span><span>Resources</span><span>Blog</span><span>Contact Us</span></nav>
        <div class="phone"><svg width="14" height="14" fill="#e4202f"><use href="#phoneIcon"/></svg>230-555-0147</div>
        <div class="hero-copy">
          <div class="pre">We are</div>
          <div class="boutique">Boutique</div>
          <h1>DIGITAL<br>AGENCY</h1>
          <p>Many desktop publishing packages and web page editors now use Lorem Ipsum as their default model text, and a search for 'lorem ipsum'</p>
          <span class="btn">Contact Us</span>
        </div>
      </section>

      <section class="section features">
        <svg class="ring" width="300" height="300" viewBox="0 0 300 300"><circle cx="150" cy="150" r="148" fill="none" stroke="#eef1f2" stroke-width="2"/></svg>
        <div class="eyebrow">Features</div>
        <div class="title">Provide Awesome Service<br>With Our Tools</div>
        <div class="cards">
          <div class="card"><h4>Connectivity<br>and transportation</h4><div class="ico" style="background:var(--teal)"><svg width="26" height="26"><use href="#chipIcon"/></svg></div><div class="rule"></div><p>long established fact that a reader will be distracted</p></div>
          <div class="card"><h4>Storage and<br>processing</h4><div class="ico" style="background:var(--red)"><svg width="26" height="26" viewBox="0 0 24 24"><ellipse cx="12" cy="6" rx="8" ry="3" fill="none" stroke="#fff" stroke-width="2"/><path d="M4 6v12c0 1.7 3.6 3 8 3s8-1.3 8-3V6M4 12c0 1.7 3.6 3 8 3s8-1.3 8-3" fill="none" stroke="#fff" stroke-width="2"/></svg></div><div class="rule"></div><p>long established fact that a reader will be distracted</p></div>
          <div class="card"><h4>Services and<br>applications</h4><div class="ico" style="background:var(--lime)"><svg width="26" height="26" viewBox="0 0 24 24"><rect x="3" y="3" width="7" height="7" fill="none" stroke="#fff" stroke-width="2"/><rect x="14" y="3" width="7" height="7" fill="none" stroke="#fff" stroke-width="2"/><rect x="3" y="14" width="7" height="7" fill="none" stroke="#fff" stroke-width="2"/><rect x="14" y="14" width="7" height="7" fill="none" stroke="#fff" stroke-width="2"/></svg></div><div class="rule"></div><p>long established fact that a reader will be distracted</p></div>
          <div class="card"><h4>Terminals and<br>devices</h4><div class="ico" style="background:var(--orange)"><svg width="26" height="26" viewBox="0 0 24 24"><rect x="3" y="4" width="18" height="12" rx="1" fill="none" stroke="#fff" stroke-width="2"/><path d="M8 20h8M12 16v4" stroke="#fff" stroke-width="2"/></svg></div><div class="rule"></div><p>long established fact that a reader will be distracted</p></div>
        </div>
      </section>

      <section class="section value">
        <div class="copy">
          <h2>Value proposition &amp;<br>Benefits</h2>
          <p class="body">It is a long established fact that a reader will be distracted by the readable content of a page when looking at its layout. The point of using Lorem Ipsum is that it has a more-or-less normal distribution of letters, as opposed to using 'Content here, content here', making it look like readable English.</p>
        </div>
        <svg class="art" width="400" height="470" viewBox="0 0 400 470" role="img" aria-label="Photo of a smiling businesswoman working at a laptop, framed by an orange shape">
          <path d="M400 0 L200 0 C120 30 110 180 160 300 C210 420 300 470 400 455 Z" fill="url(#valPhoto)"/>
          <path d="M160 120 C50 130 0 230 15 320 C30 410 130 460 230 440 C320 420 350 340 320 250 C290 160 240 110 160 120 Z" fill="url(#valOrange)" opacity=".92"/>
        </svg>
      </section>

      <section class="section problem">
        <svg class="art" width="540" height="500" viewBox="0 0 540 500" role="img" aria-label="Photo of a man focused on his laptop at a desk, tinted in teal">
          <path d="M0 60 C100 -10 330 -10 440 90 C530 180 530 370 410 450 C290 520 90 500 0 440 Z" fill="url(#probPhoto)"/>
          <path d="M230 390 C300 360 390 375 420 440 C360 490 280 490 230 470 Z" fill="#f7931e" opacity=".85"/>
        </svg>
        <div class="copy">
          <h2>Problem statement</h2>
          <p class="body">It is a long established fact that a reader will be distracted by the readable content of a page when looking at its layout. The point of using Lorem Ipsum is that it has a more-or-less normal distribution of letters, as opposed to using 'Content here, content here', making it look like readable English.</p>
        </div>
      </section>

      <section class="section packages">
        <svg class="lime-blob" width="280" height="300" viewBox="0 0 280 300"><path d="M0 0 C130 0 250 40 265 120 C280 200 170 290 0 300 Z" fill="#b5e04a"/></svg>
        <div class="eyebrow">Packages</div>
        <div class="title">The best packages for our client</div>
        <div class="plans">
          <div class="plan"><div class="name">Basic Plan</div><div class="price"><sup>$</sup>25</div><ul><li>Lorem Ipsum</li><li>is simply dummy text</li><li>the printing</li><li>and typesetting industry</li></ul><span class="btn">Get Started</span></div>
          <div class="plan featured"><div class="name">Standart Plan</div><div class="price"><sup>$</sup>55</div><ul><li>Lorem Ipsum</li><li>is simply dummy text</li><li>the printing</li><li>and typesetting industry</li></ul><span class="btn">Get Started</span></div>
          <div class="plan"><div class="name">Premium Plan</div><div class="price"><sup>$</sup>85</div><ul><li>Lorem Ipsum</li><li>is simply dummy text</li><li>the printing</li><li>and typesetting industry</li></ul><span class="btn">Get Started</span></div>
        </div>
      </section>

      <section class="section customers">
        <div class="title">Target Customers</div>
        <div class="logos">
          <div class="logo-tile"><i></i>Corvana</div>
          <div class="logo-tile"><i></i>Brisklet</div>
          <div class="logo-tile"><i></i>Tacomira</div>
          <div class="logo-tile"><i></i>Pranafeed</div>
        </div>
        <div class="pager"><i></i><i class="on"></i><i></i></div>
      </section>

      <section class="section blog">
        <div class="title">Blog</div>
        <div class="posts">
          <article class="post"><svg class="thumb" viewBox="0 0 285 190" role="img" aria-label="Photo of a team meeting around a table"><rect width="285" height="190" fill="url(#b1)"/></svg><div class="date">April 6 , 2020</div><h5>Lorem Ipsum has been the industry's standard</h5><div class="more">READ MORE</div></article>
          <article class="post"><svg class="thumb" viewBox="0 0 285 190" role="img" aria-label="Photo of a hand reviewing printed charts with a pen"><rect width="285" height="190" fill="url(#b2)"/></svg><div class="date">April 6 , 2020</div><h5>Lorem Ipsum has been the industry's standard</h5><div class="more">READ MORE</div></article>
          <article class="post"><svg class="thumb" viewBox="0 0 285 190" role="img" aria-label="Photo of colleagues collaborating in a bright office"><rect width="285" height="190" fill="url(#b3)"/></svg><div class="date">April 6 , 2020</div><h5>Lorem Ipsum has been the industry's standard</h5><div class="more">READ MORE</div></article>
        </div>
      </section>

      <section class="section contact">
        <svg class="photo" width="1200" height="475" viewBox="0 0 1200 475" role="img" aria-label="Photo of a business meeting in a modern office, with a green and orange shape behind the contact form">
          <rect width="1200" height="475" fill="url(#cPhoto)"/>
          <path d="M1200 0 L1080 0 C1120 110 1170 170 1200 180 Z" fill="#1b8a84" opacity=".6"/>
          <path d="M470 -10 C640 -30 860 20 910 140 C950 260 880 440 760 475 L520 475 C380 440 320 310 340 190 C360 80 400 0 470 -10 Z" fill="#f15a24"/>
          <path d="M440 20 C620 -20 840 20 890 140 C930 250 860 420 720 455 C570 485 400 430 350 300 C310 190 350 50 440 20 Z" fill="#8dc63f" opacity=".95"/>
        </svg>
        <div class="form">
          <h3>Contact Us</h3>
          <div class="fields"><div class="field">Your Name :</div><div class="field">Your Email :</div><div class="field">Phone :</div><div class="field">Message :</div></div>
          <span class="btn">Submit Now</span>
        </div>
      </section>

      <footer class="section footer">
        <div class="cols">
          <div class="col about">
            <h6>About</h6>
            <p>It is a long established fact that a reader will be distracted by the readable content of a page when looking at its layout.</p>
            <div class="contact-line"><svg width="12" height="12" fill="#f15a24"><use href="#phoneIcon"/></svg>Call us: +230.555.0147</div>
            <div class="contact-line"><svg width="12" height="12" viewBox="0 0 24 24"><rect x="2" y="5" width="20" height="14" rx="2" fill="#f15a24"/><path d="M2 7l10 6 10-6" fill="none" stroke="#fff" stroke-width="2"/></svg>Email: hello@lumatrel.mu</div>
            <div class="connect">CONNECT WITH US</div>
            <div class="socials"><i></i><i></i><i></i><i></i><i></i></div>
          </div>
          <div class="col"><h6>Service</h6><ul><li>Connectivity</li><li>Storage</li><li>Services</li><li>Terminals</li></ul></div>
          <div class="col"><h6>Resources</h6><ul><li>It is a long established</li><li>That a reader will be</li><li>Distracted by the readable</li><li>Content of a page</li></ul></div>
          <div class="col news"><h6>Newsletter</h6><p>Subscribe to our newsletter to receive<br>exclusive offers and wedding tips.</p><input type="text" placeholder="Enter Your mail ID"><span class="btn">Submit Now</span></div>
        </div>
        <div class="copyright">Copyright©LumaTrel All Rights Reserved.</div>
      </footer>

    </div>
  </div>
</div>

<!-- ===== mobile screen ===== -->
<div class="screen mobile">
  <svg class="m" style="top:27px" width="233" height="162" viewBox="0 0 233 162" role="img" aria-label="Photo of a small agency team gathered around a table reviewing work together">
    <path d="M0 0 L233 0 L233 120 C200 150 140 165 90 150 C45 137 10 105 0 80 Z" fill="url(#heroPhoto)"/>
    <path d="M0 60 C10 100 45 140 100 152" fill="none" stroke="#8dc63f" stroke-width="4" stroke-linecap="round"/>
  </svg>
  <div class="m m-brand"><i></i>LumaTrel</div>
  <div class="m m-menu"></div>
  <div class="m m-pre">We are</div>
  <div class="m m-boutique">Boutique</div>
  <div class="m m-h1">DIGITAL<br>AGENCY</div>
  <div class="m-btn" style="left:11px;top:286px;width:112px;height:36px">Contact Us</div>

  <div class="m m-center m-eyebrow" style="top:358px">Features</div>
  <div class="m m-center m-title" style="top:376px">Provide Awesome<br>Service<br>With Our Tools</div>
  <div class="m m-card">
    <h4>Connectivity<br>and transportation</h4>
    <div class="ico"><svg width="22" height="22"><use href="#chipIcon"/></svg></div>
    <div class="rule"></div>
    <p>long established fact that a reader will be distracted</p>
  </div>
  <div class="m m-center m-arrows" style="top:761px">‹ ›</div>

  <svg class="m" style="top:788px" width="233" height="174" viewBox="0 0 233 174" role="img" aria-label="Photo of a smiling businesswoman at a laptop, framed by an orange shape">
    <circle cx="118" cy="87" r="86" fill="url(#valPhoto)"/>
    <path d="M70 40 C20 45 5 95 15 130 C30 170 100 175 125 140 C145 110 130 40 70 40 Z" fill="url(#valOrange)" opacity=".92"/>
  </svg>
  <div class="m m-center m-h2" style="top:976px">Value proposition &amp;<br>Benefits</div>
  <div class="m m-text" style="top:1024px">It is a long established fact that a reader will be distracted by the readable content of a page when look-ing at its layout. The point of</div>

  <svg class="m" style="top:1150px" width="233" height="180" viewBox="0 0 233 180" role="img" aria-label="Photo of a man focused on his laptop, tinted in teal">
    <path d="M12 60 C30 10 150 -10 200 30 C245 70 235 150 170 172 C110 190 20 170 10 120 Z" fill="url(#probPhoto)"/>
  </svg>
  <div class="m m-center m-h2" style="top:1344px">Problem statement</div>
  <div class="m m-text" style="top:1372px">It is a long established fact that a reader will be distracted by the readable content of a page when look-ing at its layout. The point of</div>

  <div class="m m-center m-eyebrow" style="top:1502px">Packages</div>
  <div class="m m-center m-h2" style="top:1522px;line-height:24px">The best packages<br>for our client</div>
  <div class="m m-plan">
    <div class="name">Standart Plan</div>
    <div class="price"><sup>$</sup>55</div>
    <ul><li>Lorem Ipsum</li><li>is simply dummy text</li><li>the printing</li><li>and typesetting industry</li></ul>
  </div>
  <div class="m-btn" style="left:52px;top:1784px;width:113px;height:36px;background:var(--white);color:var(--orange)">Get Started</div>
  <div class="m m-center m-arrows" style="top:1855px">‹ ›</div>

  <div class="m m-center m-h2" style="top:1893px">Target Customers</div>
  <div class="m m-tile"><i></i>Tacomira</div>
  <div class="m m-center m-arrows" style="top:2023px">‹ ›</div>

  <div class="m m-center m-h2" style="top:2092px">Blog</div>
  <svg class="m m-thumb" viewBox="0 0 212 152" role="img" aria-label="Photo of a hand reviewing printed charts with a pen"><rect width="212" height="152" fill="url(#b2)"/></svg>
  <div class="m m-date">April 6 , 2020</div>
  <div class="m m-post">Lorem Ipsum has been the industry's standard</div>
  <div class="m m-more">READ MORE</div>
  <div class="m m-center m-arrows" style="top:2372px">‹ ›</div>

  <svg class="m m-contact" width="233" height="240" viewBox="0 0 233 240" role="img" aria-label="Green and orange shape behind the contact form">
    <path d="M0 40 C60 0 180 -10 233 20 L233 230 C170 250 60 240 0 210 Z" fill="#f15a24"/>
    <path d="M0 50 C60 10 170 5 233 40 L233 205 C170 235 60 230 0 195 Z" fill="#8dc63f"/>
  </svg>
  <div class="m m-center" style="top:2455px;font-size:22px;color:var(--white)">Contact Us</div>
  <div class="m m-field" style="top:2492px">Your Name :</div>
  <div class="m m-field" style="top:2516px">Your Email :</div>
  <div class="m m-field" style="top:2539px">Phone :</div>
  <div class="m m-field" style="top:2562px">Message :</div>
  <div class="m-btn" style="left:58px;top:2584px;width:117px;height:38px;background:var(--white);color:var(--orange)">Submit</div>

  <div class="m m-foot" style="left:11px;top:2703px;width:210px">
    <h6>About</h6>
    <p style="margin-top:14px">It is a long established fact that a reader will be distracted by the readable content of a page when looking at its layout.</p>
  </div>
  <div class="m m-line" style="top:2804px"><svg width="11" height="11" fill="#f15a24"><use href="#phoneIcon"/></svg>Call us: +230.555.0147</div>
  <div class="m m-line" style="top:2822px"><svg width="11" height="11" viewBox="0 0 24 24"><rect x="2" y="5" width="20" height="14" rx="2" fill="#f15a24"/><path d="M2 7l10 6 10-6" fill="none" stroke="#fff" stroke-width="2"/></svg>Email: hello@lumatrel.mu</div>
  <div class="m m-foot" style="left:11px;top:2850px"><h6 style="font-size:11px">Connect with us</h6></div>
  <div class="m m-socials"><i></i><i></i><i></i><i></i><i></i></div>

  <div class="m m-foot" style="left:11px;top:2928px"><h6>Service</h6><ul style="margin-top:12px;line-height:22px"><li style="line-height:22px">Connectivity</li><li style="line-height:22px">Storage</li><li style="line-height:22px">Services</li><li style="line-height:22px">Terminals</li></ul></div>
  <div class="m m-foot" style="left:11px;top:3064px"><h6>Resources</h6><ul style="margin-top:14px"><li style="line-height:22px">It is a long established</li><li style="line-height:22px">That a reader will be</li><li style="line-height:22px">Distracted by the readable</li><li style="line-height:22px">Content of a page</li></ul></div>
  <div class="m m-foot" style="left:11px;top:3213px;width:210px"><h6>Newsletter</h6><p style="margin-top:14px">Subscribe to our newsletter to receive exclusive offers and wedding tips.</p></div>
  <div class="m m-input">Enter Your mail ID</div>
  <div class="m-btn" style="left:11px;top:3326px;width:112px;height:38px">Submit Now</div>
  <div class="m m-copy">Copyright©LumaTrel All Rights Reserved.</div>
</div>

<div class="thanks">THANKS<br>FOR<br>WATCHING</div>

</body>
</html>
```